KWR CONSTRUCTION CO POSTCARD DESIGN

I was thinking of making a postcard for mailings by printmeadow and or by me dropping off at homes . I guess it would be used as a mailing post card and or flyer . I have had sketch harbor design my buisnes cards . The buisness card design is a different version from my signage on trucks because of space . I have a logo design . thyat i can upload . I like silver for back ground and black for logo and letters with glossy finish . I would like to have the KWR with a back drop to give it depth , it would be the same color as windows .

The file i submitted ha a design with red letters , this design is more detailed than the other and should be used . The colors should be black on a silver card glossy . The windows and maybe give the letters depth with a backdrop outline . I want to let home owners know that they can always call for consultation and and repairs or maintenance for their home .

Target Market(s)

home owners

Industry/Entity Type

Construction

Font styles to use
Other font styles liked:
• The same font as used in the picture of the sign i uploaded

Requirements
Must have
• HOME IMPROVEMENTS , MAINTENANCE AND REPAIRS , CARPENTRY , TILE PAINTING ECT

```html
<!DOCTYPE html>
<html lang="en">
<head>
<meta charset="utf-8">
<title>KWR Construction Co. Postcard</title>
<link href="https://fonts.googleapis.com/css2?family=PT+Sans+Narrow:wght@400;700&family=Tinos:ital@1&display=swap" rel="stylesheet">
<style>
  :root {
    --stage: #5e3320;
    --card: #ffffff;
    --silver-light: #f4f4f5;
    --silver: #dcdcde;
    --ink: #111111;
    --ink-soft: #3a3a3a;
    --stamp-line: #b5b5b5;
    --photo-sky: #eef1ee;
    --photo-roof: #6f747c;
    --photo-wall: #cfc4b0;
    --photo-garden: #7d9a5c;
  }
  * { margin: 0; padding: 0; box-sizing: border-box; }
  html, body { width: 1200px; height: 1000px; overflow: hidden; }
  body { background: var(--stage); position: relative; font-family: "PT Sans Narrow", "Arial Narrow", sans-serif; color: var(--ink); }

  .postcard {
    position: absolute;
    background: linear-gradient(135deg, var(--silver-light) 0%, var(--card) 35%, var(--silver) 60%, var(--card) 100%);
    overflow: hidden;
  }
  .postcard--mailing { left: 67px; top: 80px; width: 708px; height: 548px; }
  .postcard--front { left: 448px; top: 367px; width: 732px; height: 567px; }

  .facets {
    position: absolute; inset: 0;
    background: linear-gradient(160deg, rgba(255,255,255,0) 30%, rgba(200,200,205,0.35) 55%, rgba(255,255,255,0) 75%);
  }

  .house-photo { position: absolute; }
  .postcard--mailing .house-photo {
    left: 200px; top: 110px; width: 508px; height: 400px;
    background: radial-gradient(ellipse at 60% 55%, rgba(190,186,178,0.45) 0%, rgba(225,225,225,0.25) 55%, rgba(255,255,255,0) 80%);
  }
  .postcard--front .house-photo {
    left: 220px; top: 152px; width: 512px; height: 312px;
    background:
      linear-gradient(90deg, rgba(255,255,255,0.95) 0%, rgba(255,255,255,0) 20%),
      linear-gradient(0deg, rgba(255,255,255,0.9) 0%, rgba(255,255,255,0) 16%),
      linear-gradient(180deg, rgba(255,255,255,0.9) 0%, rgba(255,255,255,0) 14%),
      linear-gradient(180deg, var(--photo-sky) 0%, var(--photo-roof) 32%, var(--photo-wall) 55%, var(--photo-garden) 85%, #a8b88e 100%);
  }

  .brand {
    position: absolute; display: flex; align-items: center; gap: 10px;
    font-family: "PT Sans Narrow", "Arial Narrow", sans-serif; font-weight: 700; color: var(--ink);
  }
  .brand__square { width: 34px; height: 34px; background: var(--ink); flex: none; }
  .postcard--mailing .brand { left: 36px; top: 112px; font-size: 34px; }
  .reg-number { position: absolute; left: 80px; top: 152px; font-size: 15px; color: var(--ink-soft); }

  .postcard--front .brand { left: 37px; top: 70px; font-size: 25px; line-height: 30px; }

  .stamp-box {
    position: absolute; left: 543px; top: 23px; width: 137px; height: 142px;
    background: var(--card); border: 1px solid var(--stamp-line);
  }

  .tagline { position: absolute; left: 0; top: 0; overflow: visible; }
  .tagline text { font-family: "Tinos", "Times New Roman", serif; font-style: italic; fill: var(--ink); }

  .services { position: absolute; text-transform: uppercase; }
  .postcard--mailing .services { left: 35px; top: 288px; font-size: 23px; line-height: 28px; }
  .postcard--front .services { left: 39px; top: 230px; font-size: 25px; line-height: 29px; }

  .contact-line { position: absolute; left: 35px; top: 410px; display: flex; align-items: baseline; gap: 12px; }
  .contact-line__name { font-size: 19px; font-weight: 700; }
  .contact-line__phone { font-size: 38px; }

  .small-repairs {
    position: absolute; left: 39px; top: 416px;
    font-family: "Tinos", "Times New Roman", serif; font-style: italic; font-size: 21px;
  }
  .owner { position: absolute; left: 39px; top: 464px; }
  .owner__name { font-size: 21px; font-weight: 700; line-height: 24px; }
  .owner__phone { font-size: 41px; line-height: 44px; }

  .address { position: absolute; left: 317px; top: 480px; font-size: 17px; line-height: 29px; }
</style>
</head>
<body>

  <section class="postcard postcard--mailing" aria-label="Postcard mailing side">
    <div class="facets"></div>
    <div class="house-photo" role="img" aria-label="Faded photograph of a two-storey house with a porch and front steps"></div>

    <div class="brand"><span class="brand__square"></span>KWR CONSTRUCTION CO.</div>
    <p class="reg-number">Home improvement Reg# 170326</p>

    <div class="stamp-box" aria-label="Stamp area"></div>

    <svg class="tagline" width="708" height="548" aria-label="Enhance Repair and Maintain Your Home">
      <path id="mailLine1" d="M40 228 Q155 200 271 192" fill="none"/>
      <path id="mailLine2" d="M70 262 Q190 236 310 232" fill="none"/>
      <text font-size="25"><textPath href="#mailLine1">Enhance Repair and</textPath></text>
      <text font-size="25"><textPath href="#mailLine2">Maintain Your Home</textPath></text>
    </svg>

    <p class="services">With our<br>carpentry ,<br>tile and&nbsp; painting<br>services.</p>

    <p class="contact-line">
      <span class="contact-line__name">Dan</span>
      <span class="contact-line__phone">617-555-0148</span>
    </p>
  </section>

  <section class="postcard postcard--front" aria-label="Postcard front side">
    <div class="facets"></div>
    <div class="house-photo" role="img" aria-label="Photograph of a Victorian house with a grey roof, white porch, trees and a flowering front garden"></div>

    <div class="brand"><span class="brand__square"></span><span>KWR<br>CONSTRUCTION CO.</span></div>

    <svg class="tagline" width="732" height="567" aria-label="Maintaining and Enhancing your Home">
      <path id="frontLine1" d="M264 83 Q370 48 480 55" fill="none"/>
      <path id="frontLine2" d="M362 146 Q500 90 655 100" fill="none"/>
      <text font-size="30"><textPath href="#frontLine1">Maintaining and</textPath></text>
      <text font-size="30"><textPath href="#frontLine2">Enhancing your Home</textPath></text>
    </svg>

    <p class="services">Carpentry ,<br>tile, painting,<br>maintenance and<br>repairs.</p>

    <p class="small-repairs">We also welcome small repairs !</p>

    <div class="owner">
      <p class="owner__name">Dan Meroni</p>
      <p class="owner__phone">617-555-0148</p>
    </div>

    <p class="address">K W R Construction Co. 12 Linden Row Boston, MA 02135<br>www.kwrconstructionco.com</p>
  </section>

</body>
</html>
```